Trim Orchid - Weight management

Label for Weight management products.
Design: modern, clear, minimum design (less is more) – lifestyle product
Buyers: mainly female, young and middle age
I'm adding a number of blank labels for better understanding. The design should be made in a way that it looks like a product family. Because the weight management product series consist of about 10 products all together.

Target Market(s)

mainly female, young and middle age

Industry/Entity Type

Weight

Font styles to use
Sans Serif

Colors
e34297
0392cd
f37122

Requirements
Must have
• modern, clear, minimum design (less is more) – lifestyle product

```html
<!DOCTYPE html>
<html lang="de">
<head>
<meta charset="utf-8">
<title>Trim Orchid – Etiketten Produktfamilie</title>
<link href="https://fonts.googleapis.com/css2?family=Arimo:wght@400;700&display=swap" rel="stylesheet">
<style>
  :root{
    --magenta:#e34297;
    --blue:#0392cd;
    --orange:#f37122;
    --ink:#222;
    --stage:#808080;
    --blush:#f6c3dc;
    --paper:#ffffff;
    --rule:#b9b9b9;
    --head:#d9c9e8;
  }
  *{box-sizing:border-box;margin:0;padding:0}
  html,body{width:1200px;height:1000px;overflow:hidden}
  body{background:var(--stage);font-family:"Arimo",Arial,sans-serif;color:var(--ink);position:relative}
  .label{position:absolute;left:0;background:linear-gradient(90deg,var(--blush) 0%,var(--paper) 38%,var(--paper) 62%,var(--blush) 100%);overflow:hidden}
  .abs{position:absolute}
  .brand{position:absolute;display:flex;align-items:center;gap:6px;color:var(--blue);font-weight:700;font-size:14px;white-space:nowrap}
  .brand-dot{width:14px;height:14px;border-radius:50%;background:var(--blue)}
  .brand.small{font-size:10px;gap:4px}
  .brand.small .brand-dot{width:9px;height:9px}
  .brand.large{font-size:20px;gap:8px}
  .brand.large .brand-dot{width:20px;height:20px}
  .copy{font-size:7px;line-height:1.3}
  .copy h4{color:var(--blue);font-size:inherit;font-weight:700;margin-top:6px}
  .copy .kicker{color:var(--magenta);font-weight:700;font-size:10px;line-height:1.15}
  .product-name{position:absolute;color:var(--magenta);font-weight:700;white-space:nowrap;line-height:1}
  .product-sub{position:absolute;color:var(--orange);font-weight:700;white-space:nowrap}
  .content{position:absolute;color:var(--blue);white-space:nowrap;line-height:1.35}
  .content b{font-weight:700}
  .footnote{position:absolute;font-size:5.5px;line-height:1.3}
  table.nutrition{position:absolute;border-collapse:collapse;font-size:6.5px;line-height:1.15}
  table.nutrition th{background:var(--head);color:var(--blue);font-weight:700;text-align:right;padding:1px 2px;white-space:nowrap;vertical-align:bottom}
  table.nutrition th:first-child{text-align:left}
  table.nutrition td{padding:0 2px;text-align:right;vertical-align:top;white-space:nowrap}
  table.nutrition td:first-child{text-align:left;white-space:normal}
  table.nutrition tr.gap td{padding-top:5px}
  table.nutrition tr.line td{border-top:0.5px solid var(--rule)}
  table.nutrition td.note{white-space:normal;text-align:left}
  .tag{position:absolute;font-weight:700;font-size:9px;white-space:nowrap}
  .jar-label{position:absolute;left:815px;top:285px;width:275px;height:240px;background:var(--paper)}
</style>
</head>
<body>

<!-- Zink -->
<section class="label" style="top:0;width:660px;height:238px">
  <div class="copy abs" style="left:8px;top:6px;width:232px">
    <p class="kicker">Nahrungsergänzungsmittel mit Zink</p>
    <h4>Zutaten:</h4>
    <p>Füllstoff Cellulose, Gelatine* (Kapsel), Zinkcitrat (11,2 %), Trennmittel (Magnesiumsalze der Speisefettsäuren, Siliciumdioxid), Weiße Kapselhülle (Farbstoff E 171), Schwarze Kapselhülle (Farbstoffe E 171, E 172). * = Herkunft: Rind. (Spuren von Gluten, Hühnerei-Eiweiß, Soja und Milch (inkl. Laktose) können nicht ausgeschlossen werden.)</p>
    <h4>Verzehrempfehlung: <span style="color:var(--ink);font-weight:400">1 Kapsel pro Tag</span></h4>
    <h4 style="color:var(--magenta)">Hinweise:</h4>
    <p>Die angegebene empfohlene tägliche Verzehrmenge darf nicht überschritten werden. Nicht als Ersatz für eine ausgewogene und abwechslungsreiche Ernährung verwenden. Außerhalb der Reichweite von kleinen Kindern lagern. Auf eine abwechslungsreiche und ausgewogene Ernährung sowie eine gesunde Lebensweise sollte geachtet werden.</p>
  </div>
  <div class="content" style="left:8px;top:210px;font-size:10px">Inhalt: 180 Kapseln à 715 mg<br><b>Nettogewicht pro Dose:</b> ℮ 128,7 g</div>
  <div class="brand" style="left:290px;top:52px"><span class="brand-dot"></span>Trim Orchid</div>
  <div class="product-name" style="left:284px;top:132px;font-size:30px">ZINK</div>
  <table class="nutrition" style="left:472px;top:12px;width:183px">
    <tr><th>Nährwerte</th><th>/ 100 g</th><th>/ Kapsel</th></tr>
    <tr><td>Energie</td><td>931 kJ<br>226 kcal</td><td>6,7 kJ<br>1,6 kcal</td></tr>
    <tr class="gap"><td>Fett</td><td>1,4 g</td><td>&lt; 0,1 g</td></tr>
    <tr><td>- davon gesättigte Fettsäuren</td><td>1,3 g</td><td>&lt; 0,1 g</td></tr>
    <tr class="gap"><td>Kohlenhydrate</td><td>0,1 g</td><td>&lt; 0,1 g</td></tr>
    <tr><td>- davon Zucker</td><td>&lt; 0,1 g</td><td>&lt; 0,1 g</td></tr>
    <tr><td>Eiweiß</td><td>15,8 g</td><td>0,1 g</td></tr>
    <tr><td>Salz</td><td>&lt; 0,1 g</td><td>&lt; 0,01 g</td></tr>
    <tr class="gap"><td>Zink</td><td>3497 mg</td><td>25,0 mg</td></tr>
    <tr><td>- davon NRV*</td><td></td><td>250 %</td></tr>
    <tr class="gap"><td class="note" colspan="3">*NRV = % der Nährstoffbezugswerte<br>(nach VO (EG) Nr. 1169/2011)</td></tr>
  </table>
  <p class="footnote" style="left:472px;top:212px;width:180px">Bei Raumtemperatur (bis 21°C), trocken und vor Sonneneinstrahlung geschützt lagern. LOT-Nr. / Mindestens haltbar bis Ende: Siehe Dosenboden.</p>
</section>

<!-- Omega 3 -->
<section class="label" style="top:246px;width:660px;height:230px">
  <div class="copy abs" style="left:6px;top:4px;width:135px;font-size:6px">
    <p style="color:var(--magenta);font-weight:700">Nahrungsergänzungsmittel.</p>
    <h4>Zutaten:</h4>
    <p>Fischöl mit Omega3 Fettsäuren (18% EPA, 12% DHA); demineralisiertes Wasser, Softgel-Kapselhülle: Gelatine (Rind), Glyzerin, Vitamin E (DL-Alpha-Tocopherolacetat).</p>
    <h4>Verzehrempfehlung:</h4><p>1x zwei Kapseln pro Tag</p>
    <h4>Gesamtgewicht Kapsel: <span style="color:var(--ink);font-weight:400">1450 mg</span></h4>
    <h4 style="color:var(--magenta)">Hinweise:</h4>
    <p>Empfohlene tägliche Verzehrmenge nicht überschreiten. Nicht als Ersatz für eine ausgewogene und abwechslungsreiche Ernährung verwenden. Außerhalb der Reichweite von kleinen Kindern lagern.</p>
    <h4>Allergen-Kennzeichnung:</h4>
    <p>enthält Zutaten aus Fisch: Sardine, Makrele und Sardelle</p>
  </div>
  <div class="content" style="left:6px;top:194px;font-size:9px;line-height:2">INHALT: 200 STÜCK (À 1,450G)<br>NETTOGEWICHT PRO DOSE: ℮ 290G</div>
  <div class="brand" style="left:290px;top:32px"><span class="brand-dot"></span>Trim Orchid</div>
  <div class="product-name" style="left:235px;top:92px;font-size:44px">OMEGA 3</div>
  <div class="product-sub" style="left:276px;top:138px;font-size:13px">18 DHA &amp; 12 EPA</div>
  <table class="nutrition" style="left:540px;top:4px;width:116px;font-size:5.3px">
    <tr><th>Nährwerte</th><th>pro 100g</th><th>pro Kapsel</th></tr>
    <tr><td>Energie</td><td>799 kJ<br>(191,2<br>kcal)</td><td>11,6 kJ<br>(2,8 kcal)</td></tr>
    <tr class="line"><td>Fett</td><td>6,7 g</td><td>97 mg</td></tr>
    <tr><td>- davon gesättigte</td><td>5,3 g</td><td>77 mg</td></tr>
    <tr class="line"><td>Kohlenhydrate</td><td>26,5 g</td><td>384 mg</td></tr>
    <tr><td>- davon Zucker</td><td>&lt; 0,1 g</td><td>&lt; 0,1 mg</td></tr>
    <tr><td>Eiweiß</td><td>16,9 g</td><td>245 mg</td></tr>
    <tr><td>Salz</td><td>&lt; 0,1 g</td><td>&lt; 0,1 mg</td></tr>
    <tr class="gap"><td>Fischöl</td><td>69,0 g</td><td>1000 mg</td></tr>
    <tr class="gap"><td>- davon Omega 3</td><td>20,7 g</td><td>300 mg</td></tr>
    <tr><td>- davon EPA*</td><td>12,4 g</td><td>180 mg</td></tr>
    <tr><td>- davon DHA**</td><td>8,3 g</td><td>120 mg</td></tr>
    <tr class="gap"><td>Vitamin E</td><td>827,6 mg</td><td>12 mg</td></tr>
    <tr><td>- davon NRV***</td><td>5172 %</td><td>75 %</td></tr>
    <tr class="gap"><td class="note" colspan="3">* EPA = Eicosapentaensäure<br>** DHA = Docosahexaensäure<br>*** NRV = % der Nährstoffbezugswerte</td></tr>
  </table>
  <div class="tag" style="left:540px;top:180px">Trim Orchid Smart Dieting</div>
  <p class="footnote" style="left:540px;top:212px;width:116px;font-size:4.5px">Bei Raumtemperatur (bis 21°C), trocken und vor Sonneneinstrahlung geschützt lagern. Haltbar: Siehe Dosenboden.</p>
</section>

<!-- MSM -->
<section class="label" style="top:486px;width:660px;height:230px">
  <div class="copy abs" style="left:8px;top:6px;width:238px">
    <p class="kicker" style="font-size:12px">Nahrungsergänzungsmittel</p>
    <p class="kicker" style="font-size:8px">mit MSM, L-Tyrosin, GOS und Vitamin C</p>
    <p style="margin-top:5px"><b style="color:var(--blue)">Zutaten:</b> Methyl Sulphonyl Methan (MSM) (77,4 %), Galacto Oligosaccharide (GOS) (enthält <b>Laktose</b>) (15,2 %), Trennmittel (Calciumphosphat, Magnesiumsalze der Speisefettsäuren, Siliciumdioxid), L-Ascorbinsäure, L-Tyrosin. (Leider können aus verpackungstechnischen Gründen Spuren von Gluten, Hühnerei-Eiweiß und Soja nicht zu 100% ausgeschlossen werden.)</p>
    <h4>Verzehrempfehlung: <span style="color:var(--ink);font-weight:400">7 Tabletten pro Tag</span></h4>
    <h4 style="color:var(--magenta)">Hinweis:</h4>
    <p>Die angegebene empfohlene tägliche Verzehrmenge darf nicht überschritten werden. Nicht als Ersatz für eine ausgewogene und abwechslungsreiche Ernährung verwenden. Außerhalb der Reichweite von kleinen Kindern lagern. Auf eine abwechslungsreiche und ausgewogene Ernährung sowie eine gesunde Lebensweise sollte geachtet werden.</p>
  </div>
  <div class="content" style="left:8px;top:178px;font-size:12px;line-height:1.15"><b>Inhalt:</b> 150 Stück (à 922mg)<br><b>Nettogewicht pro Dose:</b> ℮ 138,3g</div>
  <p class="footnote" style="left:8px;top:208px;width:230px">Bei Raumtemperatur (bis 21°C), trocken und vor Sonneneinstrahlung geschützt lagern. LOT-Nr. / Mindestens haltbar bis Ende: Siehe Dosenboden</p>
  <div class="brand" style="left:290px;top:30px"><span class="brand-dot"></span>Trim Orchid</div>
  <div class="product-name" style="left:282px;top:104px;font-size:34px;font-weight:400">MSM</div>
  <div class="product-sub" style="left:282px;top:140px;font-size:8px;font-weight:400">Methylsulfonylmethan</div>
  <table class="nutrition" style="left:455px;top:6px;width:200px;font-size:6px">
    <tr><th>Nährwerte</th><th>pro 100g</th><th>pro Tablette<br>(922 mg)</th><th>pro 7 Stück<br>(6,454 mg)</th></tr>
    <tr><td>Energie</td><td>205 kJ<br>(49,9 kcal)</td><td>1,9 kJ<br>(0,5 kcal)</td><td>13,3 kJ<br>(3,2 kcal)</td></tr>
    <tr class="line"><td>Fett</td><td>1,0 g</td><td>&lt; 0,1 g</td><td>&lt; 0,1 g</td></tr>
    <tr><td>- davon gesättigte Fettsäuren</td><td>1,0 g</td><td>&lt; 0,1 g</td><td>&lt; 0,1 g</td></tr>
    <tr class="line"><td>Kohlenhydrate</td><td>4,6 g</td><td>&lt; 0,1 g</td><td>0,3 g</td></tr>
    <tr><td>- davon Zucker</td><td>4,6 g</td><td>&lt; 0,1 g</td><td>0,3 g</td></tr>
    <tr><td>Eiweiß</td><td>0,2 g</td><td>&lt; 0,1 g</td><td>&lt; 0,1 g</td></tr>
    <tr><td>Salz</td><td>&lt; 0,01g</td><td>&lt; 0,01 g</td><td>&lt; 0,01 g</td></tr>
    <tr class="gap"><td><b>Zugesetzt</b></td><td></td><td></td><td></td></tr>
    <tr><td>Methyl Sulphonyl Methan (MSM)</td><td>77440 mg</td><td>714 mg</td><td>5000 mg</td></tr>
    <tr><td>L-Tyrosin</td><td>155 mg</td><td>1,43 mg</td><td>10,0 mg</td></tr>
    <tr><td>Galacto Oligosaccharide (GOS)</td><td>15184 mg</td><td>140 mg</td><td>980 mg</td></tr>
    <tr class="gap"><td><b>Vitamine</b></td><td></td><td></td><td></td></tr>
    <tr><td>Vitamine C</td><td>184 mg</td><td>1,7 mg</td><td>12,0 mg</td></tr>
  </table>
  <div class="tag" style="left:520px;top:200px;color:var(--orange);font-weight:400">Trim Orchid Smart Dieting</div>
</section>

<!-- BCAA -->
<section class="label" style="top:726px;width:812px;height:120px">
  <div class="copy abs" style="left:22px;top:5px;width:280px;font-size:5.8px;line-height:1.25">
    <p style="color:var(--magenta);font-weight:700;font-size:6.5px">Pulver aus verzweigtkettigen Aminosäuren L-Leucin, L-Isoleucin und L-Valin und Vitamin B6. Mit Süßungsmitteln.</p>
    <p style="margin-top:4px"><b style="color:var(--blue)">Zutaten:</b> L-Leucin (30,0 %), Säuerungsmittel (Citronensäure), L-Isoleucin (15,0 %), L-Valin (15,0 %), Mais-Dextrin, Aroma, Emulgator (Soja-Lecithin), Natriumcitrat, Süßungsmittel (Sucralose, Acesulfam K), färbendes Lebensmittel Rote Bete Pulver, Verdickungsmittel (Gummi arabicum), Trennmittel (Siliciumdioxid), Pyridoxinhydrochlorid, Farbstoff (Beta-Carotin). (Spuren von Gluten, Hühnerei-Eiweiß und Milch (inkl. Laktose) können nicht ausgeschlossen werden.)</p>
    <p style="margin-top:4px"><b style="color:var(--blue)">Verzehrempfehlung:</b> 10 g Pulver in 200 ml Wasser einrühren.</p>
    <p style="margin-top:4px"><b style="color:var(--magenta)">Hinweis:</b> Nicht als Ersatz für eine ausgewogene und abwechslungsreiche Ernährung sowie gesunde Lebensweise verwenden.</p>
    <p style="margin-top:4px">LOT-Nr. / Ungeöffnet, kühl und trocken aufbewahrt mindestens haltbar bis Ende: Siehe Dosenboden</p>
  </div>
  <div class="brand small" style="left:398px;top:8px"><span class="brand-dot"></span>Trim Orchid</div>
  <div class="product-name" style="left:322px;top:32px;font-size:27px;font-weight:400">BCAA PULVER</div>
  <div class="product-sub" style="left:322px;top:60px;font-size:9.5px">L-LEUCIN + L-VALIN + L-ISOLEUCIN</div>
  <div class="tag" style="left:366px;top:92px;font-size:9px">Blutorangengeschmack</div>
  <div class="tag" style="left:382px;top:104px;font-size:10px">Inhalt: ℮ 300 g</div>
  <p class="footnote" style="left:598px;top:112px;width:100px;transform:rotate(-90deg);transform-origin:0 0;font-size:5px">BCAA – Pulver mit L-Leucin, L-Isoleucin, L-Valin und Vitamin B6</p>
  <table class="nutrition" style="left:618px;top:4px;width:190px;font-size:5.3px">
    <tr><th>Nährwerte</th><th>/ 100 g</th><th>/ 10 g</th></tr>
    <tr><td>Energie</td><td>1448 kJ (341 kcal)</td><td>144 kJ (34,1 kcal)</td></tr>
    <tr><td>Fett</td><td>&lt; 0,1 g</td><td>&lt; 0,1 g</td></tr>
    <tr><td>- davon gesättigte Fettsäuren</td><td>&lt; 0,1 g</td><td>&lt; 0,1 g</td></tr>
    <tr><td>Kohlenhydrate</td><td>5,6 g</td><td>0,6 g</td></tr>
    <tr><td>- davon Zucker</td><td>0,8 g</td><td>&lt; 0,1 g</td></tr>
    <tr><td>Ballaststoffe</td><td>11,2 g</td><td>1,1 g</td></tr>
    <tr><td>Eiweiß</td><td>60,0 g</td><td>6,0 g</td></tr>
    <tr><td>Salz</td><td>0,57 g</td><td>0,06 g</td></tr>
    <tr class="gap"><td>BCAAs* zugesetzt:</td><td>60,0 g</td><td>6,0 g</td></tr>
    <tr><td>- L-Leucin</td><td>30,0 g</td><td>3,0 g</td></tr>
    <tr><td>- L-Isoleucin</td><td>15,0 g</td><td>1,5 g</td></tr>
    <tr><td>- L-Valin</td><td>15,0 g</td><td>1,5 g</td></tr>
    <tr><td>Vitamin B6</td><td>20,0 mg (1440 %)</td><td>2,0 mg (144 %)</td></tr>
    <tr class="gap"><td class="note" colspan="3">*NRV = % der Nährstoffbezugswerte (nach VO (EU) Nr. 1169/2011)</td></tr>
  </table>
</section>

<!-- L-Glutamin -->
<section class="label" style="top:852px;width:812px;height:132px">
  <div class="copy abs" style="left:22px;top:4px;width:110px;font-size:5px">
    <p style="color:var(--magenta);font-weight:700;font-size:7.5px">L-Glutamin</p>
    <p><b style="color:var(--blue)">Zutaten:</b> L-Glutamin (100 %)</p>
    <p style="margin-top:5px"><b style="color:var(--blue)">Zubereitung:</b> 5g mit 200ml Wasser vermischen und sofort trinken.</p>
    <p style="margin-top:5px"><b style="color:var(--magenta)">Allergie-Hinweis:</b> Enthält keine potenziellen Allergene. Spuren von Gluten, Soja, Laktose und Hühnereiweiß können nicht ausgeschlossen werden.</p>
  </div>
  <div class="content" style="left:8px;top:110px;font-size:11px;font-weight:700">Inhalt: ℮ 250 g</div>
  <p class="footnote" style="left:8px;top:124px;width:500px;font-size:4.5px">Bei Raumtemperatur (bis 21°C), trocken und vor Sonneneinstrahlung geschützt lagern. LOT-Nr. / Mindestens haltbar bis Ende: Siehe Dosenboden.</p>
  <div class="brand small" style="left:388px;top:6px"><span class="brand-dot"></span>Trim Orchid</div>
  <div class="product-name" style="left:330px;top:36px;font-size:34px">L-Glutamin</div>
  <div class="product-sub" style="left:392px;top:72px;font-size:20px">Pulver</div>
  <table class="nutrition" style="left:680px;top:4px;width:126px;font-size:5.5px">
    <tr><th>Nährwerte</th><th>pro 100g</th><th>pro 5g</th></tr>
    <tr><td>Energie</td><td>1700 kJ<br>(400 kcal)</td><td>85 kJ<br>(20 kcal)</td></tr>
    <tr class="line"><td>Fett</td><td>&lt; 0,1 g</td><td>&lt; 0,1 g</td></tr>
    <tr><td>- davon gesättigte Fettsäuren</td><td>&lt; 0,1 g</td><td>&lt; 0,1 g</td></tr>
    <tr class="line"><td>Kohlenhydrate</td><td>&lt; 0,1 g</td><td>&lt; 0,1 g</td></tr>
    <tr><td>- davon Zucker</td><td>&lt; 0,1 g</td><td>&lt; 0,1 g</td></tr>
    <tr class="line"><td>Eiweiß</td><td>100,0 g</td><td>5,0 g</td></tr>
    <tr><td>- davon L-Glutamin</td><td>100,0 g</td><td>5,0 g</td></tr>
    <tr class="line"><td>Salz</td><td>&lt; 0,1 g</td><td>&lt; 0,1 g</td></tr>
  </table>
  <div class="tag" style="left:690px;top:104px;color:var(--orange);font-weight:400">Trim Orchid Smart Dieting</div>
</section>

<!-- Front label, flat -->
<section class="jar-label">
  <div class="brand large" style="left:80px;top:34px"><span class="brand-dot"></span>Trim Orchid</div>
  <div class="product-name" style="left:10px;top:98px;font-size:42px">OMEGA 3</div>
  <div class="product-sub" style="left:70px;top:150px;font-size:13px">18 DHA &amp; 12 EPA</div>
</section>

</body>
</html>
```